Brindlewick Solutions - Website for a CRM IT Services Provider to Non-profits

We need a website design for our company that provides IT services to non-profits to enable them to manage their donors and philanthropy within their organization.

We would like to see a design that uses the colors in our logo and a funky take on how to uniquely present a topic as boring as IT. Examples of sites that we really like: tamsinvoke.com, www.corabellquist.com, mintgable.com

The final design should communicate that we are a professional, yet creative company that is fun to work with.

Target Market(s)

Non-profits who tend to be young, creative types that are low-tech

Industry/Entity Type

It Company

Requirements
Must have
• Must include tabs for Home, Contact Us, About, Projects, and Blog. The site must use the logo we have attached on all of the page, in one way or another (it can be small & in the corner).

The site has to work on all mobile browsers (iphone, ipad).
Nice to have
• It would be great if I could supply some HTML for the Contact page that would allow me to capture leads and put them directly into my CRM application. It's very easy to set up.
Should not have
• The design should not use old-style fonts and should not have a lot of dark colors. Keep it similar to our logo, clean and simple. We're not looking for a busy home page.

```html
<!DOCTYPE html>
<html lang="en">
<head>
<meta charset="utf-8">
<title>Brindlewick Solutions</title>
<link rel="stylesheet" href="https://fonts.googleapis.com/css2?family=Quicksand:wght@600;700&family=Permanent+Marker&display=swap">
<style>
  :root {
    --sea-deep: #2f8ea6;
    --sea-mid: #3d9fb4;
    --sea-light: #86c9d4;
    --sea-glow: #76f2f0;
    --floor: #2a7d93;
    --nav-ink: #0f4656;
    --nav-active: #1d6275;
    --white: #ffffff;
    --foot-text: #a9d6df;
    --bubble: #9fd9e2;
  }
  * { margin: 0; padding: 0; box-sizing: border-box; }
  html, body { width: 1200px; height: 907px; overflow: hidden; }
  body {
    position: relative;
    font-family: "Quicksand", sans-serif;
    background:
      radial-gradient(ellipse 340px 170px at 600px -10px, rgba(118,242,240,0.9), rgba(118,242,240,0) 100%),
      radial-gradient(ellipse 420px 360px at 600px 520px, var(--sea-light), rgba(134,201,212,0) 100%),
      linear-gradient(180deg, var(--sea-mid), var(--sea-deep));
  }
  .brand {
    position: absolute; left: 218px; top: 24px; width: 84px;
    text-align: center; color: var(--white);
  }
  .brand-mark {
    width: 84px; height: 84px; border-radius: 50%;
    background: radial-gradient(circle at 40% 35%, #e9fbf9, #b7ebe6);
  }
  .brand-name {
    margin-top: 4px; font-size: 15px; font-weight: 600; line-height: 13px;
  }
  .main-nav {
    position: absolute; top: 54px; left: 430px;
    display: flex; list-style: none;
  }
  .main-nav li a {
    display: block; height: 36px; line-height: 37px;
    font-size: 14px; font-weight: 700; letter-spacing: 1.6px;
    color: var(--nav-ink); text-decoration: none;
  }
  .main-nav li + li { margin-left: 40px; }
  .main-nav li.active a {
    background: linear-gradient(180deg, #17566a, var(--nav-active));
    color: var(--white); padding: 0 11px;
  }
  .main-nav li.active + li { margin-left: 28px; }
  .tagline {
    position: absolute; top: 217px; left: 0; width: 1208px;
    text-align: center; color: var(--white);
    font-size: 46px; font-weight: 700; line-height: 58px; letter-spacing: 3.2px;
    text-shadow: 0 2px 3px rgba(20,70,85,0.45);
  }
  .reef {
    position: absolute; left: 210px; top: 550px; width: 760px; height: 190px;
    background: radial-gradient(ellipse 50% 55% at 55% 60%, rgba(150,210,220,0.45), rgba(150,210,220,0) 100%);
  }
  .seafloor { position: absolute; left: 0; top: 680px; width: 1200px; height: 227px; }
  .footer-mark {
    position: absolute; left: 236px; top: 740px; width: 52px; height: 52px;
    border-radius: 50%; background: rgba(160,215,225,0.55);
  }
  .copyright {
    position: absolute; left: 234px; top: 798px;
    font-family: Arial, sans-serif; font-size: 10px; color: var(--foot-text);
  }
  .connect {
    position: absolute; left: 845px; top: 755px;
    font-family: "Permanent Marker", cursive; font-size: 10px; color: var(--white);
    letter-spacing: 0.4px; text-transform: uppercase;
  }
  .social { position: absolute; left: 859px; top: 777px; display: flex; gap: 8px; list-style: none; }
  .social li {
    width: 30px; height: 30px; border-radius: 50%;
    background: radial-gradient(circle at 40% 35%, #d6f3f7, var(--bubble));
  }
</style>
</head>
<body>
  <header>
    <div class="brand">
      <div class="brand-mark"></div>
      <div class="brand-name">Brindlewick Solutions</div>
    </div>
    <nav>
      <ul class="main-nav">
        <li class="active"><a href="#">HOME</a></li>
        <li><a href="#">CONTACT US</a></li>
        <li><a href="#">ABOUT</a></li>
        <li><a href="#">PROJECTS</a></li>
        <li><a href="#">BLOG</a></li>
      </ul>
    </nav>
  </header>

  <main>
    <h1 class="tagline">WE PROVIDE IT SERVICES<br>TO NON-PROFITS<br>TO ENABLE THEM TO<br>MANAGE THEIR DONORS<br>AND PHILANTHROPY</h1>
    <div class="reef" role="img" aria-label="Soft seaweed and bubbles rising from the sea floor"></div>
  </main>

  <svg class="seafloor" viewBox="0 0 1200 227" aria-hidden="true">
    <path fill="var(--floor)" d="M0 40 Q30 14 62 36 Q110 2 150 34 Q200 8 240 36 Q290 -2 340 34 Q380 18 410 40 Q450 4 500 30 Q540 10 560 34 Q620 -12 700 24 Q760 6 800 30 Q860 -4 900 32 Q950 10 990 36 Q1040 -6 1090 28 Q1140 0 1170 24 Q1190 16 1200 20 L1200 227 L0 227 Z"/>
  </svg>

  <footer>
    <div class="footer-mark"></div>
    <p class="copyright">copyright 2012</p>
    <p class="connect">Connect with us</p>
    <ul class="social">
      <li aria-label="Social profile"></li>
      <li aria-label="Social profile"></li>
    </ul>
  </footer>
</body>
</html>
```